New SEO and Digital Marketing Company Needs Web Design

We need a web design for a new digital marketing and search engine optimisation consultancy company located in Australia called 'Bold Walrus'.

Bold Walrus helps other businesses improve their online presence through social media, search engine optimisation, and teaching businesses how to interact with clients online in a professional manner.

The web design needs to be simple but sophisticated and easy for visitors to navigate. Inspiration can be taken from the logo which is included with the brief.

Sections we would like the website to include are blog posts, FAQs, contact us, about us, and information on our services as well as a form section where potential clients can submit their details and a URL to their website for a quote or to organise a consultation. We also need the design to seamlessly incorporate social media.

A very basic example of layout has been uploaded. Feel free to use it for inspiration, but we're happy for you to come up with someone yourself.

Our current place-holder website is Joomla based.

Target Market(s)

Other businesses

Industry/Entity Type

Business Consultant

Coding

Coded - Design and coding required

Number of Pages Required

5+ page

Requirements
Must have
• Complements our logo
• Clean and sophisticated
• Blog
• Expandable and collapsible FAQs section
• Contact form where people can submit website URL as well as contact details and a message
• Able to integrate with social media
• Joomla based

```html
<!DOCTYPE html>
<html lang="en">
<head>
<meta charset="utf-8">
<title>Bold Walrus — Digital Marketing</title>
<link href="https://fonts.googleapis.com/css2?family=Open+Sans:wght@400;600;700&display=swap" rel="stylesheet">
<style>
:root{
  --purple:#5b2a6e;
  --green:#8cc63f;
  --text:#555;
  --heading:#333;
  --muted:#888;
  --line:#e2e2e2;
  --footer:#efefef;
  --bar:#2b2b2b;
  --page:#f4f4f4;
}
*{box-sizing:border-box;margin:0;padding:0}
html,body{width:768px;height:1200px;overflow:hidden}
body{background:var(--page);font-family:"Open Sans",Arial,sans-serif;color:var(--text);font-size:8px;line-height:1.5}
.page{width:640px;height:1200px;margin:0 auto;background:#fff;position:relative}
.site-header{height:118px;display:flex;align-items:center;justify-content:center}
.brand-name{font-weight:700;font-size:24px;color:var(--purple);letter-spacing:1px}
.main-nav{height:24px;background:var(--green);display:flex}
.main-nav a{color:#fff;text-decoration:none;font-size:7.5px;font-weight:600;padding:0 16px;line-height:24px;text-transform:uppercase}
.main-nav a.active{background:var(--purple)}
.hero{position:relative;height:262px;background:linear-gradient(120deg,#b9b2a6 0%,#8b8579 35%,#d8d4cc 60%,#6d6a63 100%)}
.hero-caption{position:absolute;left:0;top:98px;width:222px;background:rgba(20,20,20,.78);padding:14px 16px 16px}
.hero-caption h1{color:#fff;font-size:16px;font-weight:700;white-space:nowrap;margin-bottom:6px}
.hero-caption p{color:#ddd;font-size:6.5px;margin-bottom:10px}
.btn{display:inline-block;background:var(--green);color:#fff;font-size:7px;font-weight:700;padding:5px 10px;text-transform:uppercase}
.welcome{padding:24px 24px 0;text-align:center}
.welcome h2{font-size:21px;font-weight:400;color:var(--heading);margin-bottom:8px}
.welcome h2 span{color:var(--purple)}
.welcome p{font-size:7px;color:var(--muted);line-height:1.7}
.services{display:grid;grid-template-columns:repeat(3,1fr);gap:22px;padding:78px 0 0}
.service-photo{height:96px}
.service h3{font-size:10.5px;font-weight:400;color:var(--heading);margin:10px 0 5px}
.service p{font-size:6.5px;color:var(--muted);line-height:1.6;margin-bottom:8px}
.more{font-size:7px;font-weight:700;color:var(--purple);text-transform:uppercase}
.more::after{content:" ›";color:var(--green)}
.section-rule{border:0;border-top:1px solid var(--line);margin:40px 0 22px}
.blog h2{font-size:13px;font-weight:600;color:var(--heading);text-transform:uppercase;margin-bottom:20px}
.blog-list{display:grid;grid-template-columns:1fr 1fr;gap:28px}
.post{display:flex;gap:12px}
.post-photo{width:135px;height:96px;flex:none}
.post h4{font-size:9px;font-weight:400;color:var(--heading)}
.post time{display:block;font-size:8px;color:var(--purple);margin:3px 0 4px}
.post p{font-size:6.5px;color:var(--muted);line-height:1.6;margin-bottom:6px}
.post .learn{font-size:6.5px;font-weight:700;color:var(--purple);text-transform:uppercase}
.site-footer{position:absolute;left:0;right:0;top:1010px;height:155px;background:var(--footer);display:grid;grid-template-columns:1fr 1fr 1fr;gap:24px;padding:14px 18px}
.site-footer h5{font-size:9px;font-weight:600;color:var(--heading);text-transform:uppercase;padding-bottom:6px;border-bottom:1px solid #d6d6d6;margin-bottom:9px}
.site-footer p,.site-footer li{font-size:6.5px;color:var(--muted)}
.site-footer strong{display:block;font-size:8px;color:var(--heading);font-weight:600;margin-bottom:5px}
.contact-list,.recent-list{list-style:none}
.contact-list li{display:flex;align-items:center;gap:5px;margin-bottom:5px}
.recent-list li{padding:3px 0 3px 9px;position:relative;border-bottom:1px dotted #d6d6d6}
.recent-list li::before{content:"";position:absolute;left:0;top:7px;width:4px;height:4px;background:var(--green);border-radius:50%}
.icon{width:8px;height:8px;flex:none}
.footer-more{display:inline-block;margin-top:6px;font-size:6.5px;font-weight:700;color:var(--purple);text-transform:uppercase}
.copyright{position:absolute;left:0;right:0;bottom:0;height:35px;background:var(--bar);color:#aaa;font-size:6.5px;text-align:center;line-height:35px}
</style>
</head>
<body>
<div class="page">
  <header class="site-header">
    <span class="brand-name">BOLD WALRUS</span>
  </header>

  <nav class="main-nav">
    <a class="active">Home</a><a>About Us</a><a>SEO Services</a><a>Business Services</a><a>Website Services</a><a>FAQs</a><a>Blog</a><a>Contact Us</a>
  </nav>

  <section class="hero" role="img" aria-label="Photo of a desk with a laptop showing digital marketing, a plant and hands typing">
    <div class="hero-caption">
      <h1>DIGITAL MARKETING</h1>
      <p>Grow your brand online with smart search and social strategies built to deliver real results.</p>
      <span class="btn">Request a Quote ›</span>
    </div>
  </section>

  <main>
    <section class="welcome">
      <h2>Welcome To <span>Bold Walrus</span></h2>
      <p>We help growing businesses build a stronger online presence through search engine optimisation, social media and clear digital strategy. Our team works closely with every client to understand their goals, plan the right campaigns and measure progress along the way. From first audit to ongoing support, we keep things simple, honest and focused on results that matter to your business and your customers.</p>
    </section>

    <section class="services">
      <article class="service">
        <div class="service-photo" role="img" aria-label="Photo of a person with SEO keyword graphics" style="background:linear-gradient(135deg,#5d6570,#9aa3ad)"></div>
        <h3>SEO Services</h3>
        <p>Improve your search rankings with keyword research, on-page tuning and quality content that brings the right visitors to your site every day.</p>
        <span class="more">Read More</span>
      </article>
      <article class="service">
        <div class="service-photo" role="img" aria-label="Photo of business people shaking hands" style="background:linear-gradient(135deg,#e8ecef,#8a9098)"></div>
        <h3>Business Services</h3>
        <p>Learn how to talk with clients online in a professional way, with coaching and planning tailored to your team and your market.</p>
        <span class="more">Read More</span>
      </article>
      <article class="service">
        <div class="service-photo" role="img" aria-label="Photo of computer screens and devices on a desk" style="background:linear-gradient(135deg,#dfe5ea,#6f8496)"></div>
        <h3>Website Services</h3>
        <p>Clean, fast websites designed to convert visitors into customers, built on a platform you can easily update and grow with.</p>
        <span class="more">Read More</span>
      </article>
    </section>

    <hr class="section-rule">

    <section class="blog">
      <h2>Latest Blog</h2>
      <div class="blog-list">
        <article class="post">
          <div class="post-photo" role="img" aria-label="Photo of a businessman presenting at a board" style="background:linear-gradient(135deg,#e4e8ec,#7d8a98)"></div>
          <div>
            <h4>Simple steps to boost your rankings</h4>
            <time>April 25, 2015</time>
            <p>A quick guide to the small changes that help search engines find and trust your website more often.</p>
            <span class="learn">Learn More</span>
          </div>
        </article>
        <article class="post">
          <div class="post-photo" role="img" aria-label="Photo of a team meeting around a table from above" style="background:linear-gradient(135deg,#4a4f58,#a9adb3)"></div>
          <div>
            <h4>Building trust on social media</h4>
            <time>April 25, 2015</time>
            <p>How regular, friendly and professional posts can turn followers into loyal long term customers.</p>
            <span class="learn">Learn More</span>
          </div>
        </article>
      </div>
    </section>
  </main>

  <footer class="site-footer">
    <div>
      <h5>Contact Us</h5>
      <strong>Bold Walrus</strong>
      <ul class="contact-list">
        <li><svg class="icon" viewBox="0 0 10 10"><path d="M5 0a3.5 3.5 0 0 0-3.5 3.5C1.5 6 5 10 5 10s3.5-4 3.5-6.5A3.5 3.5 0 0 0 5 0z" fill="#5b2a6e"/><circle cx="5" cy="3.5" r="1.2" fill="#fff"/></svg>PO Box 482, Perth WA 6014</li>
        <li><svg class="icon" viewBox="0 0 10 10"><path d="M2 0h2l1 2.5-1.5 1a6 6 0 0 0 3 3l1-1.5L10 6v2a2 2 0 0 1-2 2A8 8 0 0 1 0 2a2 2 0 0 1 2-2z" fill="#5b2a6e"/></svg>(08) 5550 1742</li>
        <li><svg class="icon" viewBox="0 0 10 10"><rect x="0" y="2" width="10" height="6.5" fill="#5b2a6e"/><path d="M0 2l5 3.5L10 2" stroke="#fff" stroke-width="0.8" fill="none"/></svg>hello@boldwalrus.example</li>
      </ul>
    </div>
    <div>
      <h5>About Us</h5>
      <p>We are a small team of search and social specialists based in Australia, helping local businesses earn attention online with clear plans, honest advice and steady results over time.</p>
      <span class="footer-more">Read More</span>
    </div>
    <div>
      <h5>Recent Blog Posts</h5>
      <ul class="recent-list">
        <li>Seven quick wins for local search</li>
        <li>Why your website needs fresh content</li>
        <li>Planning a month of social posts</li>
        <li>Reading your analytics with confidence</li>
      </ul>
    </div>
  </footer>
  <div class="copyright">© 2015 Bold Walrus. All Rights Reserved.</div>
</div>
</body>
</html>
```